Album art for soul / electronic band

Album art for a singer / producer duo. Art should be similar to the copper lantern album art and be consistent with the color scheme in the attached band photo. The name of the album is corvelha (portuguese for delicate). Please do not include the photo in your design. Design should center around water.

Target Market(s)

Gen X / Millenial soul music fans

Industry/Entity Type

music

Font styles to use
Sans Serif

Requirements
Must have
• Clean modern look, photo or artwork.
Nice to have
• It should look like album art from groups in the same genre such as the Copper Lantern, Brasskite, K. Dunmore, Orrin Vale
Should not have
• band photo, musical notes, any music iconography

```html
<!DOCTYPE html>
<html lang="en">
<head>
<meta charset="utf-8">
<title>Velin Soreh — Corvelha</title>
<link rel="stylesheet" href="https://fonts.googleapis.com/css2?family=Nunito:ital,wght@1,300&display=swap">
<style>
  :root {
    --page-bg: #ffffff;
    --sky-top: #4d6674;
    --sky-mid: #8fa5a6;
    --sky-low: #cfd2c4;
    --horizon: #7d6c73;
    --water-far: #8a7f86;
    --water-mid: #6f7c84;
    --water-near: #56676f;
    --artist-ink: #0b0b0d;
    --title-ink: #d8ccd0;
  }
  html, body {
    margin: 0;
    padding: 0;
    width: 1200px;
    height: 1048px;
    overflow: hidden;
    background: var(--page-bg);
  }
  .canvas {
    position: relative;
    width: 1200px;
    height: 1048px;
  }
  .album-cover {
    position: absolute;
    left: 338px;
    top: 238px;
    width: 572px;
    height: 572px;
    overflow: hidden;
  }
  .cover-scene {
    position: absolute;
    inset: 0;
    width: 100%;
    height: 100%;
    display: block;
  }
  .artist-name,
  .album-title {
    position: absolute;
    margin: 0;
    font-family: "Nunito", "Helvetica Neue", Arial, sans-serif;
    font-style: italic;
    font-weight: 300;
    font-size: 65px;
    line-height: 1;
    letter-spacing: 0.5px;
    white-space: nowrap;
  }
  .artist-name {
    right: 38px;
    top: 439px;
    color: var(--artist-ink);
  }
  .album-title {
    left: 38px;
    top: 503px;
    color: var(--title-ink);
  }
</style>
</head>
<body>
  <main class="canvas">
    <section class="album-cover">
      <svg class="cover-scene" viewBox="0 0 572 572" role="img" aria-label="Photograph of a calm sea at low tide under a pale sky with small scattered clouds, wet sand reflecting the light">
        <defs>
          <linearGradient id="sky" x1="0" y1="0" x2="0" y2="1">
            <stop offset="0" stop-color="var(--sky-top)"/>
            <stop offset="0.5" stop-color="var(--sky-mid)"/>
            <stop offset="1" stop-color="var(--sky-low)"/>
          </linearGradient>
          <linearGradient id="water" x1="0" y1="0" x2="0" y2="1">
            <stop offset="0" stop-color="var(--horizon)"/>
            <stop offset="0.2" stop-color="var(--water-far)"/>
            <stop offset="0.6" stop-color="var(--water-mid)"/>
            <stop offset="1" stop-color="var(--water-near)"/>
          </linearGradient>
        </defs>
        <rect x="0" y="0" width="572" height="296" fill="url(#sky)"/>
        <rect x="0" y="296" width="572" height="276" fill="url(#water)"/>
      </svg>
      <h2 class="artist-name">VELIN SOREH</h2>
      <h1 class="album-title">CORVELHA</h1>
    </section>
  </main>
</body>
</html>
```